Visitenkarten-Design für Süßigkeiten-Onlineshop
Zielgruppe
Ich werde einen Onlineshop betreiben und Süßigkeiten aus aller Welt verkaufen.
Aufgabenstellung
Mein Logo sollte drauf sein. Die Visitenkarte kann auch bisschen stylischer gestaltet werden. Aber da lasse ich mich auch gerne überraschen.
Man könnte vielleicht noch den Slogan- Süßigkeiten aus aller Welt-
Mein Name sollte drauf stehen,
Jonas Brettel
Lindauer Weg 14
41562 Kastelbrück
E-Mail info@zuckerfuchs-shop.de
Instagram @zuckerfuchs.de
Facebook Zuckerfuchs
Tic Toc @zuckerfuhcs.de

```html
<!DOCTYPE html>
<html lang="de">
<head>
<meta charset="utf-8">
<title>Zuckerfuchs – Visitenkarte</title>
<link rel="stylesheet" href="https://fonts.googleapis.com/css2?family=Open+Sans:wght@400;600&display=swap">
<style>
  :root {
    --backdrop: #a9bcb5;
    --paper: #ffffff;
    --teal: #82c9cb;
    --teal-light: #b4e3e4;
    --ink: #1d1d1d;
    --ink-soft: #333333;
    --white: #ffffff;
  }
  * { box-sizing: border-box; margin: 0; padding: 0; }
  html, body {
    width: 1200px; height: 1029px; overflow: hidden;
    background: var(--backdrop);
    font-family: "Open Sans", sans-serif;
  }
  .sheet {
    position: relative; width: 1200px; height: 1029px;
    display: flex; align-items: center; justify-content: center; gap: 60px;
  }
  .card {
    width: 520px; height: 316px; background: var(--paper);
    box-shadow: 0 14px 30px rgba(40, 60, 55, .25);
    position: relative; overflow: hidden; flex: none;
  }

  /* front */
  .card--front { display: flex; align-items: center; justify-content: center; }
  .brand { display: flex; align-items: center; gap: 20px; }
  .brand__dot { width: 92px; height: 92px; border-radius: 50%; background: var(--teal); flex: none; }
  .brand__word { display: flex; flex-direction: column; align-items: center; gap: 8px; }
  .brand__rule { width: 100%; height: 1px; background: var(--ink-soft); }
  .brand__name {
    font-size: 30px; font-weight: 400; letter-spacing: 4px;
    text-transform: uppercase; color: var(--ink-soft); white-space: nowrap;
  }

  /* back */
  .card--back { display: flex; }
  .card__panel {
    width: 280px; flex: none; background: var(--teal); color: var(--white);
    padding: 30px 22px 24px 30px; position: relative;
  }
  .card__divider { width: 4px; flex: none; background: var(--teal-light); margin-left: 6px; }
  .brand--panel { gap: 12px; justify-content: center; }
  .brand--panel .brand__dot { width: 44px; height: 44px; background: var(--white); }
  .brand--panel .brand__rule { background: var(--white); }
  .brand--panel .brand__name { color: var(--white); font-size: 19px; letter-spacing: 2px; }
  .panel__web { text-align: center; font-size: 13px; margin-top: 14px; }
  .socials { list-style: none; margin-top: 24px; display: flex; flex-direction: column; gap: 12px; }
  .socials__item { display: flex; align-items: center; gap: 12px; font-size: 14px; white-space: nowrap; }
  .socials__ring { width: 28px; height: 28px; border: 2px solid var(--white); border-radius: 50%; flex: none; }

  .card__info { flex: 1; padding: 30px 18px 22px 22px; color: var(--ink); }
  .info__name { color: var(--teal-light); font-size: 22px; font-weight: 400; white-space: nowrap; }
  .info__address { font-size: 13px; line-height: 1.4; margin-top: 8px; padding-left: 20px; white-space: nowrap; }
  .info__phone { font-size: 13px; margin-top: 22px; white-space: nowrap; }
  .info__badge { margin-top: 22px; text-align: right; }
  .info__hours {
    display: inline-block; border: 2px solid var(--ink); padding: 2px 14px;
    font-size: 20px; margin-right: 20px;
  }
  .info__claim { font-size: 14px; margin-top: 8px; }
</style>
</head>
<body>
<main class="sheet">
  <section class="card card--front" aria-label="Vorderseite">
    <div class="brand">
      <span class="brand__dot"></span>
      <div class="brand__word">
        <span class="brand__rule"></span>
        <span class="brand__name">Zuckerfuchs</span>
        <span class="brand__rule"></span>
      </div>
    </div>
  </section>

  <section class="card card--back" aria-label="Rückseite">
    <div class="card__panel">
      <div class="brand brand--panel">
        <span class="brand__dot"></span>
        <div class="brand__word">
          <span class="brand__rule"></span>
          <span class="brand__name">Zuckerfuchs</span>
          <span class="brand__rule"></span>
        </div>
      </div>
      <p class="panel__web">@zuckerfuchs.de</p>
      <ul class="socials">
        <li class="socials__item"><span class="socials__ring"></span>@zuckerfuchs.de</li>
        <li class="socials__item"><span class="socials__ring"></span>Zuckerfuchs</li>
        <li class="socials__item"><span class="socials__ring"></span>@zuckerfuchs.de</li>
      </ul>
    </div>
    <span class="card__divider"></span>
    <div class="card__info">
      <h1 class="info__name">Jonas Brettel</h1>
      <p class="info__address">Lindauer Weg 14<br>41562 Kastelbrück</p>
      <p class="info__phone">Tel.Nr.: 01520 4478316</p>
      <div class="info__badge">
        <span class="info__hours">24/7</span>
        <p class="info__claim">Täglich shoppen</p>
      </div>
    </div>
  </section>
</main>
</body>
</html>
```